Hollis Ironworks Business Card

We need a business card design for a new small metal fabrication business in rural NSW, Australia.

The business (Hollis Ironworks) is owner operated by a man with the initials RB - much of the branding comes from this name.

Hollis Ironworks designs, engineers, repairs and manufactures a range of custom, quality metal works including vehicle trays, agricultural machinery impliments, trailers, wood splitters, fire pits, furniture etc.

The brand position focuses on custom work of the highest quality.

Business card design should show quality, attention to detail and stand out among a mass of business cards.

Logos are in the files

The grey color may be changed on the logo if required to stand out more.

There is an image attached of a simple card that is liked because it is clean, clear, simple, masculine and effective. It says 'quality'. As most of the work we do is custom it would be good to have the business card speak to this.

Target Market(s)

Rural and regional based Australians. Primarily adult male 25-60 yrs. Primary production / rural / travelling lifestyle.

Industry/Entity Type

Metal Fabrication

Contact Information for Business Card

The words 'custom quality fabrications' would be great somewhere perhaps on the backside (not on the information side)
Name
title
Phone: 0491 538 274 and (02) 7342 9185
email: info@hollisiw.com.au
www.hollisiw.com.au

address (2 lines)

Requirements
Nice to have
• Background colour should be very navy blue or black.
Should not have
• NO orange and blue combinations.
• Navy is OK

```html
<!DOCTYPE html>
<html lang="en">
<head>
<meta charset="utf-8">
<title>Hollis Ironworks Business Card</title>
<link rel="stylesheet" href="https://fonts.googleapis.com/css2?family=Open+Sans:wght@400;600;700&display=swap">
<style>
  :root {
    --backdrop: #0f1626;
    --card-green: #6abd45;
    --card-white: #ffffff;
    --steel-grey: #9b9b9b;
    --ink-white: #ffffff;
  }
  * { margin: 0; padding: 0; box-sizing: border-box; }
  html, body {
    width: 1200px;
    height: 987px;
    overflow: hidden;
    background: var(--backdrop);
    font-family: "Open Sans", sans-serif;
  }
  .canvas {
    position: relative;
    width: 1200px;
    height: 987px;
  }
  .card {
    position: absolute;
    left: 292px;
    width: 615px;
    height: 351px;
    overflow: hidden;
  }
  .card--front { top: 130px; background: var(--card-white); }
  .card--back { top: 505px; background: var(--card-green); }

  .front-shapes {
    position: absolute;
    inset: 0;
    width: 615px;
    height: 351px;
  }

  .front-brand {
    position: absolute;
    left: 34px;
    top: 188px;
    width: 240px;
    text-align: center;
    font-weight: 700;
    font-size: 28px;
    line-height: 1.1;
    letter-spacing: 2px;
    text-transform: uppercase;
    color: var(--steel-grey);
  }

  .holder {
    position: absolute;
    right: 38px;
    top: 45px;
    text-align: right;
    color: var(--ink-white);
  }
  .holder__name {
    font-weight: 600;
    font-size: 19px;
    letter-spacing: 0.3px;
    line-height: 26px;
  }
  .holder__title {
    font-size: 15px;
    line-height: 22px;
  }

  .contact-list {
    position: absolute;
    right: 38px;
    bottom: 40px;
    list-style: none;
    color: var(--ink-white);
    font-size: 14.5px;
    line-height: 23px;
  }
  .contact-list li {
    display: flex;
    justify-content: flex-end;
    align-items: center;
    gap: 7px;
  }
  .contact-list svg {
    width: 14px;
    height: 14px;
    fill: var(--ink-white);
    flex: none;
  }
  .contact-list .icon-spacer { width: 14px; flex: none; }

  .back-brand {
    position: absolute;
    inset: 0;
    display: flex;
    flex-direction: column;
    align-items: center;
    justify-content: center;
    text-align: center;
    color: var(--ink-white);
  }
  .back-brand__name {
    font-weight: 700;
    font-size: 40px;
    line-height: 1.08;
    letter-spacing: 3px;
    text-transform: uppercase;
  }
  .back-brand__tagline {
    margin-top: 16px;
    font-weight: 600;
    font-size: 13px;
    letter-spacing: 4px;
    text-transform: uppercase;
  }
</style>
</head>
<body>
<main class="canvas">

  <section class="card card--front" aria-label="Business card, information side">
    <svg class="front-shapes" viewBox="0 0 615 351" aria-hidden="true">
      <polygon points="223,0 615,0 615,351 223,351 344,222 344,122" fill="var(--card-green)"/>
      <polyline points="215,0 337,122 337,222 215,351" fill="none" stroke="var(--steel-grey)" stroke-width="3.5"/>
    </svg>

    <div class="front-brand">Hollis<br>Ironworks</div>

    <div class="holder">
      <p class="holder__name">MARK TANNER</p>
      <p class="holder__title">CEO/Founder</p>
    </div>

    <ul class="contact-list">
      <li>27 Anvil Lane
        <svg viewBox="0 0 24 24" aria-hidden="true"><path d="M12 2a7 7 0 0 0-7 7c0 5 7 13 7 13s7-8 7-13a7 7 0 0 0-7-7zm0 9.5A2.5 2.5 0 1 1 12 6.5a2.5 2.5 0 0 1 0 5z"/></svg>
      </li>
      <li>Tallowa NSW 2660<span class="icon-spacer"></span></li>
      <li>0491 538 274
        <svg viewBox="0 0 24 24" aria-hidden="true"><path d="M6.6 10.8a15.1 15.1 0 0 0 6.6 6.6l2.2-2.2a1 1 0 0 1 1-.25 11.4 11.4 0 0 0 3.6.57 1 1 0 0 1 1 1V20a1 1 0 0 1-1 1A17 17 0 0 1 3 4a1 1 0 0 1 1-1h3.5a1 1 0 0 1 1 1c0 1.25.2 2.45.57 3.57a1 1 0 0 1-.25 1z"/></svg>
      </li>
      <li>(02) 7342 9185
        <svg viewBox="0 0 24 24" aria-hidden="true"><path d="M6.6 10.8a15.1 15.1 0 0 0 6.6 6.6l2.2-2.2a1 1 0 0 1 1-.25 11.4 11.4 0 0 0 3.6.57 1 1 0 0 1 1 1V20a1 1 0 0 1-1 1A17 17 0 0 1 3 4a1 1 0 0 1 1-1h3.5a1 1 0 0 1 1 1c0 1.25.2 2.45.57 3.57a1 1 0 0 1-.25 1z"/></svg>
      </li>
      <li>info@hollisiw.com.au
        <svg viewBox="0 0 24 24" aria-hidden="true"><path d="M2 5h20v14H2z M3.5 6.5 12 13l8.5-6.5" fill="var(--ink-white)" stroke="var(--card-green)" stroke-width="1.4"/></svg>
      </li>
      <li>www.hollisiw.com.au
        <svg viewBox="0 0 24 24" aria-hidden="true"><circle cx="12" cy="12" r="10"/><path d="M7 7c2 0 3 1 3 3s-2 2-2 4 2 2 2 4M15 5c0 2 1 3 3 3M14 20c0-2 1-4 3-4" fill="none" stroke="var(--card-green)" stroke-width="1.6"/></svg>
      </li>
    </ul>
  </section>

  <section class="card card--back" aria-label="Business card, brand side">
    <div class="back-brand">
      <p class="back-brand__name">Hollis<br>Ironworks</p>
      <p class="back-brand__tagline">Custom quality fabrications</p>
    </div>
  </section>

</main>
</body>
</html>
```